Layout für unsere Stellenanzeigen
Zielgruppe
Wir sind spezialisiert auf die Personalvermittlung von Medizinischen Fachkräften! Krankenschwestern - Altenpfleger u.s.w....!
Aufgabenstellung
Es soll nicht überladen sein - gerne kreativ witzig. Bitte einmal über unsere Homepage schauen. Wir arbeiten mit den Farben grün grau und schwarz. Pantonen anbei! Wir haben unsere Stil komplett auf Strichmännchen - Cartoon ausgelegt. Vielleicht gibt es hier Ideen diese Strichmännchen mit Realen Bilder zu kombinieren!!??!
Anlage:

```html
<!DOCTYPE html>
<html lang="de">
<head>
<meta charset="utf-8">
<title>Stellenanzeige – Gesundheits- und Krankenpfleger/in</title>
<link rel="stylesheet" href="https://fonts.googleapis.com/css2?family=Fira+Sans:wght@400;500;800&display=swap">
<style>
  :root {
    --green: #00a04a;
    --green-dark: #3f8a3a;
    --green-light: #78b85a;
    --white: #ffffff;
    --grey: #717174;
    --grey-dark: #5f5f62;
    --text-font: "Fira Sans", Arial, sans-serif;
  }
  html, body { margin: 0; padding: 0; overflow: hidden; }
  body { width: 846px; height: 1200px; background: var(--white); font-family: var(--text-font); }
  .ad { position: relative; width: 846px; height: 1200px; overflow: hidden; background: var(--white); }

  .ad__backdrop { position: absolute; inset: 0; }

  .ad__url {
    position: absolute; left: 23px; top: 30px; margin: 0;
    color: var(--white); font-size: 31px; font-weight: 400; letter-spacing: 0.5px;
    transform: rotate(-2.2deg); transform-origin: left center;
  }

  .headline {
    position: absolute; left: 24px; top: 92px; margin: 0;
    color: var(--green); font-size: 62px; line-height: 74px; font-weight: 400;
    letter-spacing: 0.5px; transform: rotate(-2.6deg); transform-origin: left top;
  }
  .headline strong { font-weight: 800; }

  .hero-illustration {
    position: absolute; left: 624px; top: 215px; width: 200px; height: 625px;
    background: linear-gradient(180deg, #e9efe9 0%, #4fb468 40%, #2f9f55 70%, #dfe4df 100%);
    border-radius: 100px 100px 30px 30px; opacity: 0.9;
  }

  .job-title {
    position: absolute; left: 28px; top: 392px; margin: 0;
    color: var(--white); transform: rotate(-1.6deg); transform-origin: left top;
    font-size: 53px; line-height: 63px; font-weight: 800; letter-spacing: 0.5px;
  }
  .job-title .job-title__lead { display: block; font-weight: 400; font-size: 42px; line-height: 54px; }
  .job-title .job-title__light { font-weight: 400; }

  .tag-home-office {
    position: absolute; left: 394px; top: 652px; width: 216px; height: 50px;
    border: 2px dashed var(--white); border-radius: 14px;
    color: var(--white); font-size: 29px; line-height: 48px; text-align: center;
    transform: rotate(-1.6deg);
  }

  .intro {
    position: absolute; margin: 0; color: var(--green);
    font-size: 17.5px; line-height: 21px; font-weight: 500;
    transform: rotate(-2.8deg); transform-origin: left top;
    white-space: nowrap;
  }
  .intro--profile { left: 36px; top: 862px; }
  .intro--offer { left: 298px; top: 918px; }

  .footer { position: absolute; left: 0; top: 1030px; width: 846px; height: 170px; }
  .footer__band { position: absolute; inset: 0; }

  .footer__greeting {
    position: absolute; left: 26px; top: 1112px; width: 200px; height: 66px;
    background: linear-gradient(90deg, var(--grey-dark), #8a8a8d); border-radius: 6px;
  }

  .brand {
    position: absolute; left: 246px; top: 1124px; display: flex; align-items: center; gap: 6px;
    color: var(--white); font-size: 17px; font-weight: 800; line-height: 1; white-space: nowrap;
  }
  .brand__dot { width: 24px; height: 24px; border-radius: 50%; background: var(--white); }

  .footer__divider { position: absolute; left: 401px; top: 1086px; width: 2px; height: 86px; background: var(--white); }

  .contact {
    position: absolute; margin: 0; color: var(--white);
    font-size: 14px; line-height: 19px; font-style: normal; font-weight: 400;
    transform: rotate(-2.4deg); transform-origin: left top; white-space: nowrap;
  }
  .contact--address { left: 424px; top: 1080px; }
  .contact--lines { left: 606px; top: 1076px; }
</style>
</head>
<body>
<main class="ad">
  <svg class="ad__backdrop" width="846" height="1200" viewBox="0 0 846 1200" aria-hidden="true">
    <defs>
      <radialGradient id="rays" cx="0.62" cy="0.5" r="0.75">
        <stop offset="0" stop-color="#2f9a45"/>
        <stop offset="0.55" stop-color="#3f8a3a"/>
        <stop offset="1" stop-color="#6cb04e"/>
      </radialGradient>
    </defs>
    <rect class="backdrop__green" x="0" y="0" width="846" height="840" fill="url(#rays)"/>
    <polygon class="backdrop__speech-banner" fill="#ffffff"
      points="0,90 846,38 846,232 598,247 598,334 548,254 0,283"/>
    <line x1="0" y1="283" x2="548" y2="254" stroke="#00a04a" stroke-width="3"/>
    <polygon class="backdrop__white-base" fill="#ffffff" points="0,812 846,758 846,1200 0,1200"/>
  </svg>

  <p class="ad__url">www.pflegewerk-7.de</p>

  <h1 class="headline">NICHT NUR <strong>SUPERHELDEN</strong><br>TRAGEN EINEN <strong>UMHANG.</strong></h1>

  <div class="hero-illustration" role="img" aria-label="Strichmännchen-Figur einer Pflegerin mit grünem Umhang, grünem Kasack und winkender Hand"></div>

  <h2 class="job-title">
    <span class="job-title__lead">Werde</span>
    GESUNDHEITS- UND<br>
    KRANKENPFLEGER/IN<br>
    <span class="job-title__light">oder</span> KINDERKRANKEN-<br>
    PFLEGER/IN!
  </h2>
  <div class="tag-home-office">Home Office</div>

  <p class="intro intro--profile">Sie sind verantwortungsbewusst, können selbstständig<br>arbeiten, sind erfahren in der Pflege und im Umgang mit<br>chronisch Kranken?</p>
  <p class="intro intro--offer">Sie arbeiten gerne eigenveratwortlich von zu Hause<br>aus, sind trotzdem reisefreudig (Ba-Wü), schätzen einen<br>Dienstwagen der Mittelklasse - auch zur privaten Nutung<br>und suchen eine überwiegend organisatorische und<br>beratende Tätigkeit, die spannend und gut bezahlt ist?</p>

  <footer class="footer">
    <svg class="footer__band" width="846" height="170" viewBox="0 0 846 170" aria-hidden="true">
      <polygon fill="#717174" points="0,60 846,8 846,170 0,170"/>
    </svg>
  </footer>
  <div class="footer__greeting" role="img" aria-label="Handschriftzug: Wir freuen uns auf Ihre Anfrage!"></div>
  <div class="brand"><span class="brand__dot"></span><span>Pflegewerk 7</span></div>
  <div class="footer__divider"></div>
  <address class="contact contact--address">Pflegewerk 7<br>Personaldienst GmbH<br>Jonas Berger<br>Lindenhof-Allee 12<br>76530 Tannstadt</address>
  <address class="contact contact--lines">Tel: 07231- 512 448 0<br>Fax: 07231 - 512 448 9<br>Mobil: 0171 33 44 518<br>jonas.berger@pflegewerk-7.de</address>
</main>
</body>
</html>
```